Postcard designed to acquire new customers

Need a postcard style AD to place in dentist offices and other professionals to promote our tax saving system. We will place these in dentists offices, orthodontist, optometrist, physiotherapist and all sorts of medical/dental offices. The card should highlight how they can save taxes by using our software. Our website has good information on it, and I'll include the advertising PDF that our software company produces. Our logo is a little out-dated and I've included the bonus of the winner re-making the logo so its better than it currently is.
Updates

I don't need to have any space allocated for a stamp and address. We are using this to place in offices and are for advertising purposes, not mailing. Thanks!

Reason: My apologies for not providing feedback yet, I've lost several days due to some illness and am finally back at work. I'll be going through designs today and would like the extra few days to work with many of you to create a great design. Thank you for your patience! Dalmon

Reason: Again, my apologies for the delay. I will be in contact with designers this week. Thank you,

Target Market(s)

Small Business Owners in Canada

Industry/Entity Type

Health Insurance

Logo Text

Save Time, Save Money

Other font styles liked:
• Easy to Read Font's

Colors

Designer to choose colors to be used in the design.

Requirements
Must have
• Must have a call to action on the postcard to sell the service. We need people to have their attention caught. A call to action could be, "You're spending too much on taxes! That's what they'll say if your business doesn't have a Kivo Health Spending Account..."
• See the PDF for other catch phrases or key information on what a Health Spending Account is. Many people don't know so I'd like to see 3-4 bullet points on the front of the postcard on what a health spending account is. See the attached PDF for that information and simplifying the information to short bullet points would be best. Here are my thoughts:
• Who should have a Kivo Health Spending Account?
• - Every business owner who is incorporated should have one.
• - Write off 100% of this ZWK approved this method.
• - It is the most tax effective way to run dental, health, vision and other expenses through your company.
• - Easy to use APP for your phone, 2-day turnaround time for claims
• If you aren't using this, you're throwing tax dollars away!
• The back of the postcard would include 2 things. First, an example of the taxes you can save, and second - the different information they can send us so we can setup your account.
• First is the example of how this saves you money. Assuming a 38% personal tax rate. You will need to earn $1.62 of gross income, pay $0.62 of personal tax, which leaves you with $1.00 of after tax money to use for your personal expenses.
• The example of using a Kivo Health Spending Account, or doing nothing would need the following information.
• Comparison
• $5,000 of medical, dental, vision expenses
• Do Nothing Kivo Health Spending Account
• $8,100 – Total Cost $5,525 – Total Cost
• $3,100 – Income Tax $500 fee & $25 GST
• $5,000 – Money needed for medical, dental, vision, etc. $5,000 – Money needed for medical, dental, vision, etc.
• SAVINGS is $2,575
• Assuming a company incorporated in Alberta and a one time setup fee of $275 has not been included in the comparison.
• Information to send us to setup your account is:
• - Names and birth dates of you and your dependents
• - Contact information for you and your business (if different) Address, email, phone numbers
• - We will contact you about how to setup the app, your banking details and some other items.
• - Setup fee is a one-time payment of $275
Nice to have
• I'd like the front of the postcard to not be very busy with the background or graphics, etc. I want the call to action to be very obvious so they want to read the bullet points and look at the back of the postcard for more information.

```html
<!DOCTYPE html>
<html lang="en">
<head>
<meta charset="utf-8">
<title>Kivo Health Spending – Postcard</title>
<link rel="stylesheet" href="https://fonts.googleapis.com/css2?family=Open+Sans:ital,wght@0,400;0,600;0,700;0,800;1,400&display=swap">
<style>
  :root {
    --red: #ee1c25;
    --blue: #1a7bc4;
    --ink: #1e1e1e;
    --muted: #9a9a9a;
    --paper: #ffffff;
    --stage: #e6e6e6;
    --rule: #c9c9c9;
  }
  * { box-sizing: border-box; margin: 0; padding: 0; }
  html, body { width: 1200px; height: 900px; overflow: hidden; }
  body {
    background: var(--stage);
    font-family: "Open Sans", Arial, sans-serif;
    color: var(--ink);
    position: relative;
  }
  .card {
    position: absolute;
    top: 260px;
    width: 570px;
    height: 380px;
    background: var(--paper);
    overflow: hidden;
    box-shadow: 0 4px 14px rgba(0,0,0,.18);
  }
  .card--front { left: 20px; }
  .card--back { left: 610px; }
  .abs { position: absolute; }

  /* brand */
  .brand { display: flex; align-items: flex-start; gap: 8px; }
  .brand__mark { width: 30px; height: 30px; background: var(--ink); flex: none; margin-top: 2px; }
  .brand__name { color: var(--red); font-weight: 700; font-size: 17px; line-height: 1.1; }
  .brand__tag { font-style: italic; font-size: 10.5px; margin-top: 2px; text-align: right; }

  /* front */
  .front-left { left: 22px; top: 22px; width: 250px; }
  .who-title { color: var(--blue); font-weight: 700; font-size: 13px; line-height: 1.1; margin-top: 16px; }
  .bullets { list-style: none; margin-top: 4px; }
  .bullets li { font-size: 10.5px; line-height: 1.22; padding-left: 8px; position: relative; margin-bottom: 1px; }
  .bullets li::before { content: "•"; position: absolute; left: 0; }
  .divider { left: 285px; top: 24px; width: 1px; height: 236px; background: var(--ink); }
  .stamp { left: 468px; top: 20px; width: 76px; height: 76px; border: 1.5px solid var(--ink); }
  .address-line { left: 320px; width: 225px; height: 1px; background: var(--rule); }
  .stripe-right { left: 285px; top: 212px; width: 285px; height: 38px; background: var(--red); }
  .desk-figure { left: 330px; top: 130px; width: 190px; height: 116px; background: linear-gradient(180deg, #d6d6d6, #8c8c8c); }
  .throwing { left: 292px; top: 258px; width: 272px; text-align: center; color: var(--blue); font-weight: 800; font-size: 12px; line-height: 1.15; text-transform: uppercase; }
  .cta-band { left: 0; top: 262px; width: 285px; height: 58px; background: var(--red); padding: 7px 18px; }
  .cta-band__text { color: #fff; font-weight: 800; font-size: 19px; line-height: 1.05; text-transform: uppercase; }
  .cta-sub { left: 18px; top: 328px; width: 265px; color: var(--red); font-size: 12px; line-height: 1.2; }

  /* back */
  .back-left { left: 18px; top: 16px; width: 262px; }
  .example-title { color: var(--red); font-weight: 800; font-size: 14px; line-height: 1.05; text-transform: uppercase; }
  .example-body { font-size: 9.5px; line-height: 1.22; margin-top: 4px; }
  .comparison-title { color: var(--blue); font-weight: 800; font-size: 12px; text-align: center; margin-top: 6px; }
  .comparison-sub { font-size: 9.5px; text-align: center; }
  .compare { width: 100%; border-collapse: collapse; margin-top: 3px; font-size: 9.5px; line-height: 1.2; }
  .compare th { background: var(--red); color: #fff; font-weight: 700; text-align: left; padding: 2px 5px; vertical-align: top; width: 50%; }
  .compare td { padding: 2px 5px; vertical-align: top; }
  .compare .total td { border-top: 1px solid var(--ink); }
  .savings { color: var(--red); font-weight: 800; font-size: 12px; text-align: center; margin-top: 4px; text-transform: uppercase; }
  .footnote { font-size: 9.5px; line-height: 1.22; margin-top: 3px; }

  .back-right { left: 302px; top: 16px; width: 252px; }
  .info-title { color: var(--red); font-weight: 800; font-size: 13.5px; line-height: 1.05; text-transform: uppercase; margin-top: 14px; }
  .back-right .bullets li { font-size: 9.5px; }
  .piggy-photo { left: 302px; top: 222px; width: 252px; height: 146px; background: linear-gradient(160deg, #9a9a9a 0%, #4a4a4a 55%, #6b4a2e 100%); }
</style>
</head>
<body>

<section class="card card--front" aria-label="Postcard front">
  <div class="abs front-left">
    <div class="brand">
      <span class="brand__mark"></span>
      <div>
        <div class="brand__name">Kivo Health Spending</div>
        <div class="brand__tag">Save Time - Save Money</div>
      </div>
    </div>
    <h2 class="who-title">Who should have a<br>Kivo Health Spending Account?</h2>
    <ul class="bullets">
      <li>Every business owner who is incorporated should have one.</li>
      <li>Write off 100% of this ZWK approved this method.</li>
      <li>It is the most tax effective way to run dental, health, vision and other expenses through your company.</li>
      <li>Easy to use APP for your phone, 2-day turnaround time for claims</li>
    </ul>
  </div>

  <div class="abs divider"></div>
  <div class="abs stamp"></div>
  <div class="abs address-line" style="top:112px"></div>
  <div class="abs address-line" style="top:138px"></div>
  <div class="abs address-line" style="top:164px"></div>

  <div class="abs stripe-right"></div>
  <div class="abs desk-figure" role="img" aria-label="Toy businessman figure working at an office desk with a computer"></div>
  <p class="abs throwing">If you aren't using this,<br>you're throwing tax dollars away!</p>

  <div class="abs cta-band">
    <p class="cta-band__text">You're spending<br>too much on taxes!</p>
  </div>
  <p class="abs cta-sub">That's what they'll say if your business doesn't have a Kivo Health Spending Account...</p>
</section>

<section class="card card--back" aria-label="Postcard back">
  <div class="abs back-left">
    <h2 class="example-title">An example of how<br>this saves you money.</h2>
    <p class="example-body">Assuming a 38% personal tax rate. You will need to earn $1.62 of gross income, pay $0.62 of personal tax, which leaves you with $1.00 of after tax money to use for your personal expenses.<br>The example of using a Kivo Health Spending Account, or doing nothing would need the following information.</p>
    <h3 class="comparison-title">COMPARISON</h3>
    <p class="comparison-sub">$5,000 of medical, dental, vision expenses</p>
    <table class="compare">
      <tr><th>Do Nothing</th><th>Kivo Health Spending Account</th></tr>
      <tr><td>$3,100 – Income Tax</td><td>$500 fee &amp; $25 GST</td></tr>
      <tr><td>$5,000 – Money needed for medical, dental, vision, etc.</td><td>$5,000 – Money needed for medical, dental, vision, etc.</td></tr>
      <tr class="total"><td>$8,100 – Total Cost</td><td>$5,525 – Total Cost</td></tr>
    </table>
    <p class="savings">Savings is $2,575</p>
    <p class="footnote">Assuming a company incorporated in Alberta and a one time setup fee of $275 has not been included in the comparison.</p>
  </div>

  <div class="abs back-right">
    <div class="brand">
      <span class="brand__mark"></span>
      <div>
        <div class="brand__name">Kivo Health Spending</div>
        <div class="brand__tag">Save Time - Save Money</div>
      </div>
    </div>
    <h2 class="info-title">Information to send us to<br>setup your account is:</h2>
    <ul class="bullets">
      <li>Names and birth dates of you and your dependents</li>
      <li>Contact information for you and your business (if different) Address, email, phone numbers</li>
      <li>We will contact you about how to setup the app, your banking details and some other items.</li>
      <li>Setup fee is a one-time payment of $275</li>
    </ul>
  </div>
  <div class="abs piggy-photo" role="img" aria-label="Photo of a hand dropping a coin into a white piggy bank beside stacks of coins"></div>
</section>

</body>
</html>
```